Single Page Digital Brochure

We are a Sydney based finance company. We lend money to developers. Please see attached example of what we are looking to have produced. We just need a design which can be posted on LINKEDIN

Target Market(s)

Property Developers who are borrowing money

Industry/Entity Type

Finance

Requirements
Must have
• Australian relevant imagery.

TEXT TO INCLUDE:

New Offering from Harlow Ridge Capital
Nice to have
• Design and colour scheme based around our logo (attached)

Please include the same text as the attachment

Please make the design based loosely on the attachment. But do not copy the attachement
Should not have
• Remove Text: 'Settle in under four days'

```html
<!DOCTYPE html>
<html lang="en">
<head>
<meta charset="utf-8">
<title>Harlow Ridge Capital – New Offering</title>
<link href="https://fonts.googleapis.com/css2?family=Outfit:wght@300;400;600;700&display=swap" rel="stylesheet">
<style>
  :root {
    --page-bg: #eeeeee;
    --card-white: #ffffff;
    --band-grey: #57564f;
    --green-deep: #163a2c;
    --green-mid: #2c5a45;
    --green-light: #4f8a6a;
    --brand-green: #22503a;
    --text-white: #ffffff;
    --text-dark: #3b3b3b;
  }
  html, body {
    margin: 0;
    padding: 0;
    width: 1200px;
    height: 1000px;
    overflow: hidden;
    background: var(--page-bg);
    font-family: "Outfit", sans-serif;
  }
  .brochure {
    position: absolute;
    left: 204px;
    top: 259px;
    width: 800px;
    height: 456px;
    background: var(--card-white);
    overflow: hidden;
  }
  .brochure__shapes {
    position: absolute;
    inset: 0;
  }
  .headline {
    position: absolute;
    left: 40px;
    top: 44px;
    margin: 0;
    color: var(--text-white);
    font-weight: 600;
    font-size: 49px;
    line-height: 56px;
    letter-spacing: 0.5px;
    text-transform: uppercase;
  }
  .tagline {
    position: absolute;
    left: 501px;
    top: 71px;
    padding-left: 12px;
    border-left: 4px solid var(--text-white);
    margin: 0;
    color: var(--text-white);
    font-weight: 600;
    font-size: 20px;
    line-height: 27px;
  }
  .loan-terms {
    position: absolute;
    left: 500px;
    top: 152px;
    margin: 0;
    padding: 0;
    list-style: none;
    color: var(--text-white);
    font-size: 13px;
    line-height: 17.2px;
    font-weight: 300;
  }
  .loan-terms strong { font-weight: 600; }
  .contact {
    position: absolute;
    left: 40px;
    top: 372px;
    margin: 0;
    color: var(--text-dark);
    font-size: 21px;
    font-weight: 300;
    line-height: 28px;
  }
  .contact strong { color: var(--brand-green); font-weight: 600; }
  .brand {
    position: absolute;
    left: 572px;
    top: 372px;
    display: flex;
    align-items: center;
    gap: 10px;
    color: var(--brand-green);
    font-size: 19px;
    font-weight: 600;
  }
  .brand__dot {
    width: 22px;
    height: 22px;
    border-radius: 50%;
    background: var(--brand-green);
  }
</style>
</head>
<body>
  <article class="brochure">
    <svg class="brochure__shapes" width="800" height="456" viewBox="0 0 800 456">
      <defs>
        <linearGradient id="harbourTone" x1="0" y1="0" x2="0.3" y2="1">
          <stop offset="0" stop-color="#1f4a3a"/>
          <stop offset="0.45" stop-color="#2f6048"/>
          <stop offset="0.7" stop-color="#1e4536"/>
          <stop offset="1" stop-color="#143528"/>
        </linearGradient>
      </defs>
      <g role="img" aria-label="Night photograph of Sydney Harbour with the Opera House and city skyline, green-tinted">
        <path d="M0 0 H800 V290 Q720 350 560 353 L240 353 Q80 350 0 290 Z" fill="url(#harbourTone)"/>
      </g>
      <path d="M0 14 Q0 0 14 0 H786 Q800 0 800 14 Z" fill="var(--band-grey)"/>
      <path d="M0 456 V452 Q4 443 20 443 H780 Q796 443 800 452 V456 Z" fill="var(--band-grey)"/>
    </svg>

    <h1 class="headline">New Offering<br>from<br>Harlow Ridge<br>Capital</h1>

    <p class="tagline">Easy Process.<br>Quick Turnaround.</p>

    <ul class="loan-terms">
      <li><strong>Loan Amount:</strong> $750,000</li>
      <li><strong>Rate:</strong> 7.79%</li>
      <li><strong>Term:</strong> 12 months</li>
      <li><strong>LVR:</strong> 60%</li>
      <li><strong>Repayments:</strong> Capitalised</li>
      <li><strong>Turnaround:</strong> Settled in 4 days</li>
      <li><strong>Security:</strong> 2x Sydney Residential Properties</li>
      <li><strong>Purpose:</strong> Business Working Capital</li>
    </ul>

    <p class="contact">Call Us Today on <strong>1300 555 014</strong> or<br><strong>info@harlowridgecapital.com</strong></p>

    <div class="brand">
      <span class="brand__dot"></span>
      <span class="brand__name">Harlow Ridge Capital</span>
    </div>
  </article>
</body>
</html>
```